Maple. Crest PT Tri-Fold

An on demand house call mobile physical therapy and wellness company. Focused on quality rehabilitation management health and wellness needs to your door.
We need a tri-fold brochure to describe our services

Target Market(s)

Patients in need of physical therapy

Industry/Entity Type

Physical Therapy

Font styles to use
Serif
Sans Serif
Other font styles liked:
• Attached is some necessary content from a prior brochure

Colors
0054AA
0677BA
7BADD7
CADEEF
E8F1F8
EB3D1F
EC4F4E
F09395
F8D3D4
FCEDEE

```html
<!DOCTYPE html>
<html lang="en">
<head>
<meta charset="utf-8">
<title>Maple Crest PT Tri-Fold</title>
<link href="https://fonts.googleapis.com/css2?family=Montserrat:wght@400;500;600;800&display=swap" rel="stylesheet">
<style>
:root{
  --blue-deep:#0054AA;
  --blue:#0677BA;
  --blue-soft:#7BADD7;
  --blue-pale:#CADEEF;
  --blue-mist:#E8F1F8;
  --red:#EB3D1F;
  --page-bg:#C8C9C9;
  --ink:#2b2b2b;
  --white:#ffffff;
}
*{box-sizing:border-box;margin:0;padding:0}
html,body{width:824px;height:1200px;overflow:hidden}
body{background:var(--page-bg);font-family:"Montserrat",Arial,sans-serif;position:relative;color:var(--ink)}
.side-label{position:absolute;left:0;width:824px;text-align:center;font-size:20px;font-weight:400;color:#333;letter-spacing:.5px}
.side-label.front{top:30px}
.side-label.inside{top:600px}
.brochure{position:absolute;left:79px;width:665px;height:510px;overflow:hidden;background:var(--white);outline:1px solid #9a9a9a}
.brochure.front{top:62px}
.brochure.inner{top:627px}
.layer{position:absolute;display:block}
.fold{position:absolute;top:0;width:8px;height:510px;background:linear-gradient(90deg,rgba(0,0,0,0),rgba(0,0,0,.10),rgba(0,0,0,0));pointer-events:none}

/* front panel one */
.insurance-title{position:absolute;left:20px;top:34px;font-size:19px;line-height:23px;font-weight:800;color:var(--white);letter-spacing:.3px}
.insurance-note{position:absolute;left:20px;top:92px;font-size:11.5px;line-height:16.5px;font-weight:500;color:var(--white)}

/* front panel two */
.brand-name{position:absolute;font-weight:600;color:var(--blue);white-space:nowrap}
.front .brand-name.cover{left:217px;width:225px;top:370px;text-align:center;font-size:23px}
.contact-list{position:absolute;left:270px;top:427px;list-style:none}
.contact-list li{display:flex;align-items:center;height:17.5px;font-size:11px;font-weight:500;color:#222}
.contact-list .badge{width:9px;height:9px;border-radius:50%;background:var(--blue);color:var(--white);font-size:6px;font-weight:800;display:inline-flex;align-items:center;justify-content:center;margin-right:9px}

/* front panel three */
.tagline{position:absolute;left:484px;top:347px;font-size:15.5px;line-height:18.5px;font-weight:800;color:var(--blue-deep)}
.tagline-body{position:absolute;left:484px;top:386px;width:170px;font-size:11px;line-height:13.6px;font-weight:500;color:#222}
.front .brand-name.back{left:484px;top:470px;font-size:17px}

/* inside panel one */
.name-tab{position:absolute;left:16px;top:11px;width:116px;height:34px;background:var(--white)}
.inner .brand-name.tab{left:26px;top:24px;font-size:10.5px}
.intro{position:absolute;left:26px;top:57px;width:190px;font-size:12.3px;line-height:21.2px;font-weight:500;color:var(--blue)}
.intro strong{font-weight:800;color:var(--blue-deep)}

/* inside panel two */
.benefits{position:absolute;left:231px;top:41px;width:196px;list-style:none}
.benefits li{position:relative;padding-left:24px;font-size:8.8px;line-height:13.5px;font-weight:500;color:#222;text-align:justify;margin-bottom:6px}
.benefits li svg{position:absolute;left:0;top:2px;width:15px;height:14px}

/* inside panel three */
.programs-title{position:absolute;left:442px;width:223px;top:241px;text-align:center;font-size:16.5px;line-height:21px;font-weight:800;color:var(--white);letter-spacing:.3px}
.program{position:absolute;width:76px;text-align:center}
.program .ring{display:block;margin:0 auto;width:40px;height:40px}
.program span{display:block;margin-top:3px;font-size:7.8px;font-weight:500;color:var(--white);white-space:nowrap}
.program-note{position:absolute;left:589px;top:457px;font-size:9.2px;line-height:11.3px;font-weight:800;color:var(--white)}
</style>
</head>
<body>

<div class="side-label front">FRONT</div>

<section class="brochure front">
  <!-- panel one artwork -->
  <svg class="layer" style="left:0;top:0" width="217" height="510" viewBox="154 121 420 988">
    <defs>
      <linearGradient id="clinicTones" x1="0" y1="0" x2="1" y2="1">
        <stop offset="0" stop-color="#e9eef2"/><stop offset=".5" stop-color="#d9c3b4"/><stop offset="1" stop-color="#f3f4f6"/>
      </linearGradient>
    </defs>
    <rect x="154" y="121" width="420" height="607" fill="var(--blue-deep)"/>
    <path d="M300,121 C430,150 530,230 574,345 L574,121 Z" fill="var(--blue-pale)"/>
    <path d="M330,121 C440,160 520,230 574,330 L574,345 C530,240 440,160 300,121 Z" fill="var(--white)"/>
    <g fill="var(--white)">
      <rect x="191" y="401" width="123" height="46"/><rect x="323" y="401" width="97" height="46"/><rect x="429" y="401" width="98" height="46"/>
      <rect x="191" y="465" width="123" height="47"/><rect x="323" y="465" width="122" height="47"/><rect x="453" y="465" width="85" height="47"/>
      <rect x="191" y="528" width="123" height="47"/><rect x="323" y="528" width="122" height="47"/><rect x="455" y="528" width="65" height="88"/>
      <rect x="191" y="590" width="85" height="47"/><rect x="286" y="590" width="141" height="47"/>
      <rect x="191" y="655" width="123" height="47"/><rect x="323" y="655" width="101" height="47"/>
    </g>
    <rect x="154" y="728" width="420" height="381" fill="url(#clinicTones)" role="img" aria-label="Photo of a clinician holding a patient's hands across a desk"/>
  </svg>

  <!-- panels two and three artwork -->
  <svg class="layer" style="left:217px;top:0" width="448" height="510" viewBox="574 121 868 988">
    <defs>
      <linearGradient id="homeTherapyTones" x1="0" y1="0" x2="1" y2="1">
        <stop offset="0" stop-color="#eef1f0"/><stop offset=".45" stop-color="#b8bfc9"/><stop offset=".7" stop-color="#8d93a8"/><stop offset="1" stop-color="#dfe2e4"/>
      </linearGradient>
      <linearGradient id="blueShade" x1="0" y1="0" x2="1" y2="1">
        <stop offset="0" stop-color="var(--blue)"/><stop offset="1" stop-color="var(--blue-deep)"/>
      </linearGradient>
    </defs>
    <rect x="574" y="121" width="868" height="988" fill="url(#homeTherapyTones)" role="img" aria-label="Photo of a therapist stretching a patient's leg in a living room"/>
    <polygon points="574,180 610,230 574,280" fill="var(--blue-mist)"/>
    <polygon points="574,270 1057,815 1009,865 574,1109" fill="url(#blueShade)"/>
    <polygon points="1009,745 1192,688 1442,790 1442,1109 1009,1109" fill="var(--blue-mist)"/>
    <polygon points="1192,688 1442,280 1442,785" fill="url(#blueShade)"/>
    <polygon points="585,860 790,632 1009,845 1009,1109 585,1109" fill="var(--white)"/>
  </svg>

  <div class="fold" style="left:213px"></div>
  <div class="fold" style="left:438px"></div>

  <h2 class="insurance-title">ACCEPTED<br>INSURANCES:</h2>
  <p class="insurance-note">Incudes all ADVANTAGE,<br>LTC, and STATECARE plans:</p>

  <p class="brand-name cover">Maple Crest PT</p>
  <ul class="contact-list">
    <li><span class="badge">P</span>(555) 201-4830</li>
    <li><span class="badge">F</span>(555) 201-4831</li>
    <li><span class="badge">E</span>hello@maplecrestpt.com</li>
    <li><span class="badge">W</span>www.maplecrestpt.com</li>
  </ul>

  <h2 class="tagline">PHYSICAL THERAPY,<br>DELIVERED TO YOU</h2>
  <p class="tagline-body">Finding the right rehabilitation setting shapes recovery Convenient support and expert therapist</p>
  <p class="brand-name back">Maple Crest PT</p>
</section>

<div class="side-label inside">INSIDE</div>

<section class="brochure inner">
  <!-- panels one and two artwork -->
  <svg class="layer" style="left:0;top:0" width="442" height="510" viewBox="154 1214 855 988">
    <defs>
      <linearGradient id="exerciseTones" x1="0" y1="0" x2="1" y2="1">
        <stop offset="0" stop-color="#9aa6ad"/><stop offset=".35" stop-color="#1f3f73"/><stop offset=".65" stop-color="#cbb59a"/><stop offset="1" stop-color="#6fb3cf"/>
      </linearGradient>
    </defs>
    <rect x="154" y="1214" width="855" height="988" fill="var(--blue-mist)"/>
    <rect x="154" y="1214" width="855" height="29" fill="var(--blue-deep)"/>
    <path d="M515,1270 C525,1250 535,1245 560,1245 L1009,1245 L1009,1270 Z" fill="var(--blue-pale)"/>
    <path d="M154,1790 C250,1730 320,1690 375,1688 C430,1690 470,1755 560,1790 C700,1842 880,1862 1009,1858 L1009,2202 L154,2202 Z" fill="var(--blue-deep)"/>
    <path d="M157,1850 C250,1790 320,1730 378,1716 C440,1722 480,1785 580,1815 C720,1855 890,1872 1005,1868 L1005,2198 L157,2198 Z" fill="url(#exerciseTones)" role="img" aria-label="Photo of a therapist guiding a senior man lifting dumbbells while another patient uses a resistance band"/>
  </svg>

  <!-- panel three artwork -->
  <svg class="layer" style="left:442px;top:0" width="223" height="510" viewBox="1009 1214 433 988">
    <defs>
      <linearGradient id="clinicVisitTones" x1="0" y1="0" x2="1" y2="1">
        <stop offset="0" stop-color="#dfe6ec"/><stop offset=".5" stop-color="#8fb0c8"/><stop offset="1" stop-color="#2f6fb3"/>
      </linearGradient>
      <linearGradient id="programsBg" x1="0" y1="0" x2="0" y2="1">
        <stop offset="0" stop-color="var(--blue-deep)"/><stop offset="1" stop-color="var(--blue)"/>
      </linearGradient>
    </defs>
    <rect x="1009" y="1214" width="433" height="988" fill="var(--white)"/>
    <path d="M1009,1214 L1442,1214 L1442,1232 C1250,1240 1090,1320 1009,1470 Z" fill="var(--blue-deep)"/>
    <path d="M1009,1470 C1090,1320 1250,1240 1442,1232 L1442,1250 C1260,1262 1100,1350 1009,1520 Z" fill="var(--blue-soft)"/>
    <path d="M1009,1560 C1100,1390 1250,1290 1442,1268 L1442,1662 L1009,1662 Z" fill="url(#clinicVisitTones)" role="img" aria-label="Photo of a nurse with a clipboard speaking with a senior woman in a wheelchair"/>
    <rect x="1009" y="1662" width="433" height="540" fill="url(#programsBg)"/>
  </svg>

  <div class="fold" style="left:434px"></div>
  <div class="fold" style="left:213px"></div>

  <div class="name-tab"></div>
  <p class="brand-name tab">Maple Crest PT</p>
  <p class="intro"><strong>OUR HOME-BASED</strong> outpatient <strong>PHYSICAL THERAPY</strong> delivers high quality therapy services in the comfort of your own home.<br>Patients are not required to be “homebound,” as they would in the home health setting.</p>

  <ul class="benefits">
    <li><svg viewBox="0 0 15 14"><path d="M1 7 L6 12 L14 1" fill="none" stroke="var(--blue)" stroke-width="2.6" stroke-linecap="round" stroke-linejoin="round"/></svg>Not having to arrange for someone to drive them to a clinic</li>
    <li><svg viewBox="0 0 15 14"><path d="M1 7 L6 12 L14 1" fill="none" stroke="var(--blue)" stroke-width="2.6" stroke-linecap="round" stroke-linejoin="round"/></svg>The privacy that comes from one-on-one care</li>
    <li><svg viewBox="0 0 15 14"><path d="M1 7 L6 12 L14 1" fill="none" stroke="var(--blue)" stroke-width="2.6" stroke-linecap="round" stroke-linejoin="round"/></svg>Building a treatment plan around how they live</li>
    <li><svg viewBox="0 0 15 14"><path d="M1 7 L6 12 L14 1" fill="none" stroke="var(--blue)" stroke-width="2.6" stroke-linecap="round" stroke-linejoin="round"/></svg>The use of the home to provide space for exercise in order to build commitment to a home exercise plan</li>
    <li><svg viewBox="0 0 15 14"><path d="M1 7 L6 12 L14 1" fill="none" stroke="var(--blue)" stroke-width="2.6" stroke-linecap="round" stroke-linejoin="round"/></svg>The sense of independence gained from getting better and gaining function in the home</li>
    <li><svg viewBox="0 0 15 14"><path d="M1 7 L6 12 L14 1" fill="none" stroke="var(--blue)" stroke-width="2.6" stroke-linecap="round" stroke-linejoin="round"/></svg>The sense of family that comes from knowing you have a skilled clinician who knows the ins and outs of your home and your loved one's challenges and can be reached when you need them.</li>
  </ul>

  <h2 class="programs-title">REHABILITATION<br>PROGRAMS:</h2>

  <div class="program" style="left:450px;top:296px"><svg class="ring" viewBox="0 0 40 40"><circle cx="20" cy="20" r="18.5" fill="var(--blue)" stroke="var(--white)" stroke-width="1.6"/><circle cx="20" cy="20" r="7" fill="none" stroke="var(--white)" stroke-width="1.4"/></svg><span>Geriatrics</span></div>
  <div class="program" style="left:520px;top:296px"><svg class="ring" viewBox="0 0 40 40"><circle cx="20" cy="20" r="18.5" fill="var(--blue)" stroke="var(--white)" stroke-width="1.6"/><circle cx="20" cy="20" r="7" fill="none" stroke="var(--white)" stroke-width="1.4"/></svg><span>Neurological</span></div>
  <div class="program" style="left:582px;top:296px"><svg class="ring" viewBox="0 0 40 40"><circle cx="20" cy="20" r="18.5" fill="var(--blue)" stroke="var(--white)" stroke-width="1.6"/><circle cx="20" cy="20" r="7" fill="none" stroke="var(--white)" stroke-width="1.4"/></svg><span>Orthopedics</span></div>

  <div class="program" style="left:450px;top:364px"><svg class="ring" viewBox="0 0 40 40"><circle cx="20" cy="20" r="18.5" fill="var(--blue)" stroke="var(--white)" stroke-width="1.6"/><circle cx="20" cy="20" r="7" fill="none" stroke="var(--white)" stroke-width="1.4"/></svg><span>Sports Medicine</span></div>
  <div class="program" style="left:520px;top:364px"><svg class="ring" viewBox="0 0 40 40"><circle cx="20" cy="20" r="18.5" fill="var(--blue)" stroke="var(--white)" stroke-width="1.6"/><circle cx="20" cy="20" r="7" fill="none" stroke="var(--white)" stroke-width="1.4"/></svg><span>Post-Operative</span></div>
  <div class="program" style="left:582px;top:364px"><svg class="ring" viewBox="0 0 40 40"><circle cx="20" cy="20" r="18.5" fill="var(--blue)" stroke="var(--white)" stroke-width="1.6"/><path d="M20 29 C11 22 10 17 13 14 C16 11 19 13 20 15 C21 13 24 11 27 14 C30 17 29 22 20 29 Z" fill="var(--white)"/></svg><span>CHF</span></div>

  <div class="program" style="left:450px;top:433px"><svg class="ring" viewBox="0 0 40 40"><circle cx="20" cy="20" r="18.5" fill="var(--blue)" stroke="var(--white)" stroke-width="1.6"/><circle cx="20" cy="20" r="7" fill="none" stroke="var(--white)" stroke-width="1.4"/></svg><span>Balance/Vestibular</span></div>
  <div class="program" style="left:520px;top:433px"><svg class="ring" viewBox="0 0 40 40"><circle cx="20" cy="20" r="18.5" fill="var(--blue)" stroke="var(--white)" stroke-width="1.6"/><circle cx="20" cy="20" r="7" fill="none" stroke="var(--white)" stroke-width="1.4"/></svg><span>COPD</span></div>
  <p class="program-note">Home safety<br>and fall<br>prevention</p>
</section>

</body>
</html>
```